Business Card Design Quandong Celebration Crafters

on the front i would like to see the logo and my contact details. on the back i would like it to include the 3 parts to the business party planning, party hire and party supplies also with a line at the bottom (or white space) to write their appointment details.

Target Market(s)

mums and corporates

Industry/Entity Type

Business

Requirements
Must have
• logo and contact details which are: Name: Rosalind, Phone: 0417365920, email: ros@quandongfetes.com.au, Website: www.quandongfetes.com.au,

```html
<!DOCTYPE html>
<html lang="en">
<head>
<meta charset="utf-8">
<title>Quandong Celebration Crafters – Business Cards</title>
<link rel="stylesheet" href="https://fonts.googleapis.com/css2?family=Roboto+Condensed:wght@400;500&family=Questrial&display=swap">
<style>
  :root {
    --stage: #000000;
    --card: #ffffff;
    --cyan: #05c3fb;
    --magenta: #fb4af3;
    --yellow: #fdc91c;
    --ink: #4a1fb8;
    --illustration-a: #c7a58a;
    --illustration-b: #e9c7e8;
  }
  * { box-sizing: border-box; margin: 0; padding: 0; }
  html, body {
    width: 1200px; height: 1000px; overflow: hidden;
    background: var(--stage);
  }
  .stage { position: relative; width: 1200px; height: 1000px; }

  .card {
    position: absolute;
    background: var(--card);
    overflow: hidden;
    font-family: "Roboto Condensed", "Arial Narrow", sans-serif;
    color: var(--ink);
  }
  .card-front { left: 107px; top: 167px; width: 567px; height: 331px; }
  .card-back  { left: 532px; top: 534px; width: 574px; height: 338px; }

  .stripes { position: absolute; inset: 0; width: 100%; height: 100%; }
  .stripe-cyan { fill: var(--cyan); }
  .stripe-magenta { fill: var(--magenta); }
  .stripe-yellow { fill: var(--yellow); }

  /* Front */
  .mascot-art {
    position: absolute;
    border-radius: 40px 40px 8px 8px;
    background: linear-gradient(160deg, var(--illustration-b) 0%, var(--illustration-a) 70%);
  }
  .card-front .mascot-art { left: 290px; top: 24px; width: 148px; height: 122px; }
  .brand-name {
    position: absolute; left: 230px; top: 150px; width: 270px;
    text-align: center;
    font-weight: 500; font-size: 30px; line-height: 32px;
    color: var(--ink);
  }
  .contact-band {
    position: absolute; left: 78px; top: 237px; width: 489px; height: 43px;
    background: var(--yellow);
    display: flex; align-items: center; gap: 6px;
    padding-left: 14px;
    white-space: nowrap;
  }
  .contact-name, .contact-phone { font-size: 21px; }
  .contact-email { font-size: 19px; }
  .dot {
    display: inline-block; width: 12px; height: 12px; border-radius: 50%;
    flex: none;
  }
  .dot-cyan { background: var(--cyan); }
  .dot-magenta { background: var(--magenta); }
  .website {
    position: absolute; left: 180px; top: 282px; width: 372px;
    text-align: center; font-size: 22px;
  }

  /* Back */
  .appointment-title {
    position: absolute; left: 110px; top: 47px; width: 232px;
    text-align: center;
    font-family: "Questrial", sans-serif; font-size: 18px; letter-spacing: 0.5px;
  }
  .title-rule {
    position: absolute; left: 23px; width: 420px; height: 2px;
  }
  .title-rule-cyan { top: 70px; background: var(--cyan); }
  .title-rule-magenta { top: 73px; background: var(--magenta); }
  .appointment-box {
    position: absolute; left: 23px; top: 76px; width: 420px; height: 171px;
    border-left: 1px solid var(--yellow);
    border-top: 1px solid var(--yellow);
  }
  .card-back .mascot-art { left: 33px; top: 149px; width: 115px; height: 98px; }
  .services-band {
    position: absolute; left: 0; top: 247px; width: 498px; height: 44px;
    background: var(--yellow);
    clip-path: polygon(0 0, 478px 0, 498px 44px, 0 44px);
    display: flex; align-items: center; gap: 8px;
    padding-left: 26px;
    font-size: 20px; white-space: nowrap;
  }
  .services-band .service + .dot { margin-left: 4px; }
</style>
</head>
<body>
<main class="stage">

  <section class="card card-front" aria-label="Business card front">
    <svg class="stripes" viewBox="0 0 567 331" aria-hidden="true">
      <polygon class="stripe-cyan" points="0,81 93,0 170,0 0,295"/>
      <polygon class="stripe-magenta" points="176,0 193,0 43,331 0,331 0,300"/>
      <polygon class="stripe-yellow" points="197,0 207,0 58,331 48,331"/>
    </svg>
    <div class="mascot-art" role="img" aria-label="Illustration of a cartoon mascot holding party balloons"></div>
    <div class="brand-name">Quandong Celebration Crafters</div>
    <div class="contact-band">
      <span class="contact-name">Rosalind</span>
      <span class="dot dot-cyan"></span>
      <span class="contact-phone">0417365920</span>
      <span class="dot dot-magenta"></span>
      <span class="contact-email">ros@quandongfetes.com.au</span>
    </div>
    <div class="website">www.quandongfetes.com.au</div>
  </section>

  <section class="card card-back" aria-label="Business card back">
    <svg class="stripes" viewBox="0 0 574 338" aria-hidden="true">
      <polygon class="stripe-cyan" points="403,0 480,0 574,84 574,300"/>
      <polygon class="stripe-magenta" points="378,0 399,0 574,306 574,338 530,338"/>
      <polygon class="stripe-yellow" points="366,0 376,0 528,338 518,338"/>
    </svg>
    <h2 class="appointment-title">Appointment Details</h2>
    <div class="title-rule title-rule-cyan"></div>
    <div class="title-rule title-rule-magenta"></div>
    <div class="appointment-box"></div>
    <div class="mascot-art" role="img" aria-label="Small illustration of a cartoon mascot holding party balloons"></div>
    <div class="services-band">
      <span class="service">Business Party Planning</span>
      <span class="dot dot-magenta"></span>
      <span class="service">Party Hire</span>
      <span class="dot dot-cyan"></span>
      <span class="service">Party Supplies</span>
    </div>
  </section>

</main>
</body>
</html>
```